Business Card design for construction company

I would like a business card design for a construction company - Harlow Constructions. I have attached the ai logo file for use. I would like the card to be very smart and clean and incorporate only white and the two colours in the logo. I would like the card to have two sides. One side can just have the logo, the other with the relevant information.

Target Market(s)

Building and Construction Clients

Industry/Entity Type

Business

Contact Information for Business Card

Name: Tom Pardoe
Company: Harlow Constructions Pty Limited
Address: 14 Mallee Crescent Carrow Vale 2093
Phone: 0427 531 068
Email: tomp@harlowbuild-example.com.au

Font styles to use
Serif
Sans Serif

Requirements
Must have
• Details noted above
• Logo as provided
• Colours as in logo
• Square edges
• A font that compliments the logo
Should not have
• Any colour other than white and those in logo
• Rounded edges

```html
<!DOCTYPE html>
<html lang="en">
<head>
<meta charset="utf-8">
<title>Harlow Constructions – Business Card</title>
<link rel="stylesheet" href="https://fonts.googleapis.com/css2?family=Open+Sans:wght@400;600&display=swap">
<style>
  :root {
    --ink: #2b2b2b;
    --brand-blue: #0a9fc6;
    --blue-soft: #6cc6df;
    --grey-soft: #8a8a8a;
    --paper: #ffffff;
    --frame: #555555;
    --card-edge: #6b6b6b;
  }
  * { margin: 0; padding: 0; box-sizing: border-box; }
  html, body {
    width: 1054px;
    height: 1200px;
    overflow: hidden;
    background: var(--paper);
    font-family: "Open Sans", Arial, sans-serif;
    color: var(--ink);
  }
  .sheet {
    position: relative;
    width: 1054px;
    height: 1200px;
    border: 1px solid var(--frame);
  }
  .card {
    position: absolute;
    left: 131px;
    width: 793px;
    height: 453px;
    border: 1px solid var(--card-edge);
    background: var(--paper);
    overflow: hidden;
  }
  .card--front { top: 104px; }
  .card--back { top: 643px; }
  .card__decor {
    position: absolute;
    left: 0;
    right: 0;
    bottom: 0;
    height: 118px;
    background: linear-gradient(100deg, var(--brand-blue) 0%, var(--blue-soft) 45%, var(--grey-soft) 100%);
    opacity: 0.85;
  }
  .wordmark {
    position: absolute;
    left: 62px;
    top: 172px;
    font-weight: 600;
    font-size: 35px;
    letter-spacing: 5px;
    line-height: 46px;
    color: var(--ink);
    white-space: nowrap;
  }
  .contact {
    position: absolute;
    left: 63px;
    top: 70px;
  }
  .contact__name {
    font-weight: 400;
    font-size: 39px;
    line-height: 50px;
    margin-bottom: 42px;
  }
  .contact__list {
    display: grid;
    grid-template-columns: 96px auto;
    font-size: 20.5px;
    line-height: 24px;
  }
  .contact__label { white-space: nowrap; }
  .contact__value { white-space: nowrap; }
  .contact__value::before { content: ": "; }
  .contact__value--email a {
    color: var(--brand-blue);
    text-decoration: none;
  }
</style>
</head>
<body>
<main class="sheet">
  <section class="card card--front" aria-label="Card front">
    <div class="card__decor" role="img" aria-label="Decorative curved band in blue and grey"></div>
    <p class="wordmark">HARLOW CONSTRUCTIONS</p>
  </section>

  <section class="card card--back" aria-label="Card back">
    <div class="card__decor" role="img" aria-label="Decorative curved band in blue and grey"></div>
    <div class="contact">
      <h1 class="contact__name">Tom Pardoe</h1>
      <dl class="contact__list">
        <dt class="contact__label">Company</dt>
        <dd class="contact__value">Harlow Constructions Pty Limited</dd>
        <dt class="contact__label">Address</dt>
        <dd class="contact__value">14 Mallee Crescent Carrow Vale 2093</dd>
        <dt class="contact__label">Phone</dt>
        <dd class="contact__value">0427 531 068</dd>
        <dt class="contact__label">Email</dt>
        <dd class="contact__value contact__value--email"><a href="mailto:tomp@harlowbuild-example.com.au">tomp@harlowbuild-example.com.au</a></dd>
      </dl>
    </div>
  </section>
</main>
</body>
</html>
```